Branding Postcard for Real Estate Brokerage

I am a Real Estate Broker looking for a template postcard that I can use with lots of types of situations , solds, listed property, etc but has a standard layout that is consistent so it will be recognizable and tied to me. There was one that was on the template group that caught my eye. I was thinking of using the A in my logo as the script or watermark. I have uploaded my idea on that as well as other logos, etc. My goal is to have a template that I can add text to and market different things / sales / request action for pricing, etc.

Target Market(s)

Homeowners in Neighborhoods where I have sold homes

Industry/Entity Type

Real Estate

Requirements
Must have
• Area to add label for mailing, Area in front has to be a template where I can write specifics of the mailing, Consistent branding

```html
<!DOCTYPE html>
<html lang="en">
<head>
<meta charset="utf-8">
<title>Just Sold – Harborline Real Estate Brokerage Postcard</title>
<link rel="stylesheet" href="https://fonts.googleapis.com/css2?family=Arimo:wght@400;500&display=swap">
<style>
  :root {
    --brand-blue: #2e2f8a;
    --paper: #ebe9dc;
    --band-text: #f1efe5;
    --photo-fill: #524a47;
    --photo-fill-light: #5d5451;
  }
  html, body {
    margin: 0;
    padding: 0;
    width: 1200px;
    height: 930px;
    overflow: hidden;
    background: #ffffff;
  }
  .postcard {
    position: relative;
    width: 1200px;
    height: 930px;
    background: var(--paper);
    font-family: "Arimo", Arial, sans-serif;
    overflow: hidden;
  }
  .header-band {
    position: absolute;
    left: 0;
    top: 57px;
    width: 1200px;
    height: 123px;
    background: var(--brand-blue);
  }
  .headline {
    position: absolute;
    left: 64px;
    top: 18px;
    margin: 0;
    font-weight: 400;
    font-size: 72px;
    line-height: 1;
    font-variant: small-caps;
    letter-spacing: -1px;
    color: var(--band-text);
  }
  .offer-title {
    position: absolute;
    left: 63px;
    top: 284px;
    margin: 0;
    font-weight: 400;
    font-size: 55px;
    line-height: 1;
    letter-spacing: -0.5px;
    color: var(--brand-blue);
  }
  .photo-slot {
    position: absolute;
    left: 665px;
    width: 467px;
    height: 282px;
    background: linear-gradient(160deg, var(--photo-fill-light), var(--photo-fill));
  }
  .photo-slot--top { top: 232px; }
  .photo-slot--bottom { top: 544px; }
  .brokerage-name {
    position: absolute;
    left: 68px;
    top: 712px;
    margin: 0;
    font-weight: 400;
    font-size: 36px;
    line-height: 1;
    font-variant: small-caps;
    letter-spacing: -1.6px;
    color: var(--brand-blue);
  }
  .brokerage-phone {
    position: absolute;
    left: 68px;
    top: 773px;
    margin: 0;
    font-weight: 400;
    font-size: 32px;
    line-height: 1;
    letter-spacing: -1.8px;
    color: var(--brand-blue);
  }
  .brand-lockup {
    position: absolute;
    left: 320px;
    top: 790px;
    display: flex;
    align-items: center;
    gap: 12px;
  }
  .brand-lockup__dot {
    width: 18px;
    height: 18px;
    border-radius: 50%;
    background: var(--brand-blue);
  }
  .brand-lockup__name {
    font-weight: 400;
    font-size: 38px;
    line-height: 1;
    color: var(--brand-blue);
  }
  .brand-lockup__tagline {
    position: absolute;
    left: 322px;
    top: 836px;
    margin: 0;
    font-weight: 400;
    font-size: 20px;
    line-height: 1;
    letter-spacing: 0.5px;
    color: var(--brand-blue);
  }
  .footer-band {
    position: absolute;
    left: 0;
    top: 868px;
    width: 1200px;
    height: 62px;
    background: var(--brand-blue);
  }
</style>
</head>
<body>
  <main class="postcard">
    <header class="header-band">
      <h1 class="headline">Just Sold</h1>
    </header>

    <h2 class="offer-title">SPECIAL OFFER</h2>

    <div class="photo-slot photo-slot--top" role="img" aria-label="Property photo: exterior of the sold home"></div>
    <div class="photo-slot photo-slot--bottom" role="img" aria-label="Property photo: interior or second view of the sold home"></div>

    <p class="brokerage-name">Harborline Real Estate Brokerage</p>
    <p class="brokerage-phone">555-014-2287</p>

    <div class="brand-lockup">
      <span class="brand-lockup__dot"></span>
      <span class="brand-lockup__name">Harborline</span>
    </div>
    <p class="brand-lockup__tagline">Real Estate Brokerage</p>

    <footer class="footer-band"></footer>
  </main>
</body>
</html>
```